Banner Ad for Resume Services Website

The add is for this web site: www.BrightCareerPages.net

The site offers 4 different services:

- Resume Writing (by a Certified Professional Resume Writer)
- Resume Posting (posts your resume to 85 job sites)
- Resume Distribution (sends your resume to hundreds of recruiters)
- Resume Online website (created an online resume with a domain name to your name)

Colors to be used are Blue, Yellow, etc... please check the website for inspiration.

Check the web site to learn more.

Target Market(s)

Unemployed, Professionals who want to switch jobs, etc..

Industry/Entity Type

Requirements
Must have
• We definitely one this to be included on the banner:

"Free Resume Samples"

in order to attract clicks.
Nice to have
• Some of the words we suggest to include on the banner are:

"How Good is Your Resume? Ask a Professional !"

Should not have
• No animation !

Do not place the LOGO on the banner as our LOGO might change in the near future. If you already submitted a banner with the LOGO on it, you can replace it with any other graphic that has a Resume/Jobs/BusinessStaff related theme.

```html
<!DOCTYPE html>
<html lang="en">
<head>
<meta charset="utf-8">
<title>Free Resume Samples – Banner</title>
<link href="https://fonts.googleapis.com/css2?family=Cinzel:wght@400;600&family=Arimo:wght@700&family=Tinos:ital@1&display=swap" rel="stylesheet">
<style>
  :root {
    --sky-top: #3f97db;
    --sky-mid: #d6eef9;
    --sky-glow: #f4fbff;
    --sky-bottom: #86c7ec;
    --panel-blue: #1d4f93;
    --panel-edge: #123b75;
    --white: #ffffff;
    --title-glow: #2f8a3c;
    --tagline-blue: #1f3d8c;
    --stair-blue: #2d63c4;
    --stair-light: #8db4ee;
    --figure-dark: #2a2a33;
    --url-dark: #1b2a44;
  }
  * { margin: 0; padding: 0; box-sizing: border-box; }
  html, body { width: 1200px; height: 148px; overflow: hidden; background: var(--white); }
  .banner {
    position: relative;
    width: 1200px;
    height: 148px;
    overflow: hidden;
    background: linear-gradient(180deg,
      var(--sky-top) 0%,
      #7fbde8 28%,
      var(--sky-mid) 50%,
      var(--sky-glow) 58%,
      #bfe3f5 74%,
      var(--sky-bottom) 100%);
  }
  .services {
    position: absolute;
    left: 0; top: 0;
    width: 232px; height: 148px;
    background: linear-gradient(180deg, #2a62a8 0%, var(--panel-blue) 55%, var(--panel-edge) 100%);
    border-top-right-radius: 44px 74px;
    border-bottom-right-radius: 44px 74px;
    box-shadow: 3px 0 6px rgba(10, 40, 90, 0.35);
    padding: 16px 0 0 12px;
    list-style: none;
  }
  .services li {
    font-family: "Arimo", Arial, sans-serif;
    font-weight: 700;
    font-size: 17px;
    line-height: 28px;
    color: var(--white);
    white-space: nowrap;
  }
  .headline {
    position: absolute;
    left: 287px; top: 40px;
    width: 560px;
    text-align: center;
    font-family: "Cinzel", "Trajan Pro", serif;
    font-weight: 600;
    font-size: 44px;
    line-height: 50px;
    letter-spacing: 1px;
    white-space: nowrap;
    color: var(--white);
    text-shadow: 0 0 6px var(--title-glow), 0 0 2px var(--title-glow);
  }
  .tagline {
    position: absolute;
    left: 272px; top: 94px;
    width: 560px;
    text-align: center;
    font-family: "Tinos", Georgia, serif;
    font-style: italic;
    font-size: 27px;
    line-height: 32px;
    white-space: nowrap;
    color: var(--tagline-blue);
  }
  .stairway {
    position: absolute;
    left: 930px; top: 0;
    width: 270px; height: 140px;
    background: linear-gradient(200deg, var(--stair-light) 0%, var(--stair-blue) 60%, #1c4592 100%);
    clip-path: polygon(0 100%, 100% 100%, 100% 0, 88% 0, 45% 70%, 0 88%);
    opacity: 0.9;
  }
  .walker {
    position: absolute;
    left: 866px; top: 16px;
    width: 56px; height: 128px;
    background: linear-gradient(180deg, #4b4b57 0%, var(--figure-dark) 100%);
    border-radius: 22px 22px 6px 6px;
    opacity: 0.85;
  }
  .site-url {
    position: absolute;
    right: 6px; bottom: 3px;
    font-family: "Arimo", Arial, sans-serif;
    font-weight: 700;
    font-size: 13px;
    color: var(--url-dark);
  }
</style>
</head>
<body>
  <div class="banner">
    <ul class="services">
      <li>Resume Writing</li>
      <li>Resume Posting</li>
      <li>Resume Distribution</li>
      <li>Resume Online website</li>
    </ul>

    <h1 class="headline">Free Resume Samples</h1>
    <p class="tagline">How Good is Your Resume? Ask a Proffesional</p>

    <div class="stairway" role="img" aria-label="Illustration of a blue staircase curving up toward the sky"></div>
    <div class="walker" role="img" aria-label="Illustration of a businessman in a dark suit carrying a briefcase, walking toward the stairs"></div>

    <p class="site-url">www.BrightCareerPages.net</p>
  </div>
</body>
</html>
```